Ginger Beer Can Design for a none alcoholic bavarage

We need a cool, modern, fresh design for a can.

- 330ml sleek can size
- 0.0% alcohol
- BIO
- ingredience: Water, Sugar, Ginger, limejuice, Gummi Arabicum, Carbonisation
- Energy table of fats, carbs, protein, etc.
- address: Quiet Meadow Drinks, Lindenweg 42, 4052 Basel

```html
<!DOCTYPE html>
<html lang="en">
<head>
<meta charset="utf-8">
<title>BIO Non-Alcoholic Beverage – Can Label</title>
<link href="https://fonts.googleapis.com/css2?family=Oswald:wght@400;500&family=Roboto+Condensed:wght@400;500;700&family=Open+Sans:wght@400;600&display=swap" rel="stylesheet">
<style>
  :root {
    --band-black: #0b0b0b;
    --white: #ffffff;
    --green-top: #4fa830;
    --green-deep: #0b3b1d;
    --yellow: #d8c51c;
    --orange: #d9871a;
    --panel-line: #ffffff;
    --badge-red: #d32027;
    --art-lemon: #e9c630;
    --art-ginger: #b98a52;
  }
  * { box-sizing: border-box; margin: 0; padding: 0; }
  html, body {
    width: 1182px; height: 1200px; overflow: hidden;
    background: var(--white);
  }
  .label {
    position: absolute; left: 20px; top: 305px;
    width: 1142px; height: 590px;
  }
  .band {
    position: absolute; left: 0; width: 100%;
    background: var(--band-black); overflow: hidden; white-space: nowrap;
    color: var(--white);
    font: 600 14.5px/1 "Open Sans", sans-serif; letter-spacing: 1.2px;
    display: flex; align-items: center; padding-left: 16px;
  }
  .band-top { top: 0; height: 36px; }
  .band-bottom { top: 557px; height: 33px; }
  .wrap-body {
    position: absolute; left: 0; top: 41px; width: 100%; height: 512px;
    background: linear-gradient(180deg,
      var(--green-top) 0%, #2c7a28 14%, var(--green-deep) 36%,
      #3c6a1c 55%, var(--yellow) 76%, var(--orange) 100%);
  }
  .brand {
    position: absolute; left: 225px; top: 40px; width: 320px;
    color: var(--white); font-family: "Oswald", sans-serif; font-weight: 500;
    text-align: center;
  }
  .brand-name { font-size: 118px; line-height: 130px; letter-spacing: 6px; }
  .brand-sub { font-size: 21px; line-height: 24px; letter-spacing: 1px; margin-top: 8px; white-space: nowrap; }
  .product-art {
    position: absolute; left: 184px; top: 227px; width: 393px; height: 175px;
    border-radius: 80px;
    background: radial-gradient(ellipse at 28% 45%, var(--art-lemon) 0%, rgba(233,198,48,0.4) 30%, transparent 55%),
                radial-gradient(ellipse at 75% 50%, var(--art-ginger) 0%, rgba(185,138,82,0.4) 32%, transparent 58%);
  }
  .volume {
    position: absolute; left: 300px; top: 440px; width: 180px; text-align: center;
    color: var(--white); font: 500 28px/1 "Oswald", sans-serif; letter-spacing: 1px;
  }
  .nutrition {
    position: absolute; left: 609px; top: 24px; width: 248px; height: 304px;
    border: 1.5px solid var(--panel-line); border-radius: 16px; padding: 9px;
  }
  .nutrition-box {
    border: 3px solid var(--panel-line); border-radius: 9px; height: 100%;
    color: var(--white); font-family: "Roboto Condensed", sans-serif;
    display: flex; flex-direction: column; padding: 0 4px 4px;
  }
  .nutrition-title { font-size: 21px; font-weight: 500; text-align: center; line-height: 25px; border-bottom: 3px solid var(--panel-line); }
  .serving-size { font-size: 12.5px; font-weight: 700; line-height: 19px; padding-left: 3px; border-bottom: 3px solid var(--panel-line); }
  .servings { font-size: 12.5px; line-height: 16.5px; padding: 2px 3px; border-bottom: 3px solid var(--panel-line); }
  .servings li { list-style: none; display: flex; justify-content: space-between; padding-right: 40px; }
  .servings li::after { content: ""; width: 9px; height: 10px; border: 1.5px solid var(--white); border-radius: 2px; margin-top: 4px; }
  .facts { display: grid; grid-template-columns: 80px 72px 1fr; grid-template-rows: auto 1fr; flex: 1; }
  .facts > div { border-right: 3px solid var(--panel-line); }
  .facts > div:nth-child(3n) { border-right: none; }
  .facts .head { font-size: 11.5px; line-height: 14px; text-align: center; padding: 5px 0 4px; border-bottom: 3px solid var(--panel-line); }
  .facts .col { font-size: 12.5px; line-height: 16.8px; padding-top: 3px; }
  .facts .col.num { text-align: center; }
  .facts .col.names { padding-left: 3px; }
  .blurb {
    position: absolute; left: 612px; top: 340px; width: 243px;
    color: var(--white); font: 400 9.2px/11.5px "Open Sans", sans-serif; text-align: justify;
  }
  .blurb p { text-indent: 14px; }
  .marks { position: absolute; left: 612px; top: 418px; display: flex; align-items: center; gap: 6px; }
  .mark-stack { display: flex; flex-direction: column; gap: 6px; }
  .origin-badge {
    width: 40px; height: 40px; border-radius: 50%; background: var(--white);
    display: flex; align-items: center; justify-content: center;
  }
  .origin-badge span { width: 26px; height: 26px; border-radius: 50%; background: var(--badge-red); }
  .address { color: var(--white); font: 400 9.5px/11.5px "Open Sans", sans-serif; margin-left: 4px; }
</style>
</head>
<body>
<main class="label">
  <div class="band band-top">Company Name Brewing Co -Company Name Brewing Co -Company Name Brewing Co -Company Name Brewing Co -Company Name Brewing Co -</div>

  <section class="wrap-body">
    <div class="brand">
      <div class="brand-name">BIO</div>
      <div class="brand-sub">NONE ALCOHOLIC BAVARAGE</div>
    </div>

    <div class="product-art" role="img" aria-label="Photo of fresh lemons with leaves, ginger roots and a bowl of gum arabic crystals"></div>

    <div class="volume">250 ML</div>

    <div class="nutrition">
      <div class="nutrition-box">
        <div class="nutrition-title">Nutrition Information</div>
        <div class="serving-size">Serving Size: 20g (1 Tablespoon)</div>
        <ul class="servings">
          <li>- Servings per 250g jar: 12.5</li>
          <li>- Servings per 500g jar: 25.0</li>
          <li>- Servings per 1kg jar: 50.0</li>
        </ul>
        <div class="facts">
          <div class="head"></div>
          <div class="head">Average Qty<br>per Serving</div>
          <div class="head">Average Qty<br>per 100g</div>
          <div class="col names">Energy<br>Protein<br>Fat, total<br>&nbsp;- saturated<br>Carbohydrate<br>&nbsp;- sugars<br>Sodium</div>
          <div class="col num">272kJ<br>0.08g<br>0g<br>0g<br>15.9g<br>15.6g<br>2.4mg</div>
          <div class="col num">1360kJ<br>0.38g<br>0g<br>0g<br>79.6g<br>78.1g<br>12mg</div>
        </div>
      </div>
    </div>

    <div class="blurb">
      <p>Lorem ipsum dolor sit amet, consectetuer adipiscing elit, sed diam nonummy nibh euismod tincidunt ut laoreet dolore magna aliquam erat volutpat.</p>
      <p>ingredience: Water, Sugar, Ginger, limejuice, Gummi Arabicum, Carbonisation</p>
    </div>

    <div class="marks">
      <div class="mark-stack">
        <svg width="20" height="18" viewBox="0 0 20 18" aria-label="Recycling symbol">
          <g fill="none" stroke="#fff" stroke-width="2.4" stroke-linejoin="round">
            <path d="M7 4 L10 1 L13 6"/><path d="M16 9 L18 14 L12 15"/><path d="M5 15 L2 13 L5 8"/>
          </g>
        </svg>
        <svg width="22" height="14" viewBox="0 0 22 14" aria-label="Conformity mark">
          <rect x="1" y="1" width="20" height="12" fill="none" stroke="#fff" stroke-width="1.8" rx="2"/>
        </svg>
      </div>
      <div class="origin-badge" aria-label="Origin badge"><span></span></div>
      <div class="address">Quiet Meadow Drinks,<br>Lindenweg 42, 4052 Basel<br>hello@quietmeadow.ch</div>
    </div>
  </section>

  <div class="band band-bottom">Company Name Brewing Co -Company Name Brewing Co -Company Name Brewing Co -Company Name Brewing Co -Company Name Brewing Co -</div>
</main>
</body>
</html>
```